Website Design Project for Beauty & Wellness Professionals

As background information, I have a website that is focused on Beauty & Wellness Professionals:
- Job Search (www.trilhavelora.com)
- Business Classifieds (negocios.trilhavelora.com)
- Freelancer Classifieds (freelancer.trilhavelora.com)
- Course Reviews (cursos.trilhavelora.com)

All those websites use standard templates.

I need a DESIGN for the HOME PAGE (no coding) of the Website Platform that consolidates the four platforms under the same design.

Website designs that we like:
- nestorly.com
- workpane.com

Target Market(s)

Brazilian Professionals from Beauty & Wellness sector

Industry/Entity Type

Business

Requirements
Must have
• Website designs that we like:
- nestorly.com
- workpane.com

```html
<!DOCTYPE html>
<html lang="en">
<head>
<meta charset="utf-8">
<title>Trilha Velora – Home</title>
<link href="https://fonts.googleapis.com/css2?family=Arimo:wght@400;700&display=swap" rel="stylesheet">
<style>
:root{
  --teal:#2a9ab0;
  --nav:#6e7b74;
  --nav-line:#8a958f;
  --ink:#333;
  --ink-soft:#555;
  --muted:#888;
  --page:#ececec;
  --panel:#f8f8f8;
  --line:#b8b8b8;
  --red:#f25b5b;
  --green:#6bcf7f;
  --blue:#5b9bd5;
  --blue-head:#5672b3;
  --orange:#f0a04b;
  --white:#fff;
}
*{box-sizing:border-box;margin:0;padding:0}
html,body{width:1200px;height:2609px;overflow:hidden}
body{position:relative;background:var(--page);font-family:"Arimo",Arial,sans-serif;color:var(--ink)}
.abs{position:absolute}

.masthead{left:0;top:0;width:1200px;height:134px;background:var(--white)}
.brand{position:absolute;left:0;right:0;top:84px;display:flex;align-items:center;justify-content:center;gap:12px}
.brand-dot{width:28px;height:28px;border-radius:50%;background:var(--teal)}
.brand-name{font-size:34px;line-height:40px;color:var(--teal);font-weight:400}

.main-nav{left:0;top:134px;width:1200px;height:49px;background:var(--nav);display:flex;align-items:center;font-size:16px;color:var(--white)}
.main-nav span{padding:0 7px;height:49px;line-height:49px;border-right:1px solid var(--nav-line);white-space:nowrap}
.main-nav .spacer{flex:1;border:none}
.main-nav span.last{border-right:none}
.main-nav span.first-right{border-left:1px solid var(--nav-line);padding:0 14px}

.hero{left:0;top:183px;width:1200px;height:614px;background:linear-gradient(160deg,#6f8f3c 0%,#9cb55a 35%,#7f9a45 60%,#5b7a2e 100%)}
.search-bar{left:164px;top:667px;width:885px;height:76px;border-radius:38px;background:rgba(200,200,200,.55);display:flex;align-items:center;padding:0 10px 0 30px;gap:12px}
.search-type{font-size:18px;color:#666;width:98px;display:flex;align-items:center;gap:8px;border-right:1px solid #aaa;height:76px}
.search-type svg{width:18px;height:14px}
.search-field{width:278px;height:54px;background:#f2f2f2;border:1px solid #ddd}
.search-btn{margin-left:36px;width:124px;height:56px;background:var(--orange);color:var(--white);font-weight:700;font-size:19px;display:flex;align-items:center;justify-content:center;border-radius:4px}

.hero-gap{left:0;top:797px;width:1200px;height:157px;background:var(--white);box-shadow:0 8px 14px rgba(0,0,0,.28)}

.eyebrow{left:2px;top:992px;font-size:19px;color:#555}
.listing-title{left:2px;top:1033px;font-size:19px;color:#555}
.rss{left:593px;top:1026px;width:26px;height:26px;border-radius:4px;background:var(--orange)}
.rule{height:1px;background:var(--line)}

.job{position:absolute;left:0;width:637px;border-bottom:1px solid var(--line);padding:8px 45px 0 115px}
.badge{position:absolute;left:4px;top:10px;width:95px;height:31px;color:var(--white);font-size:12px;line-height:13px;text-align:center;display:flex;align-items:center;justify-content:center}
.badge.registered{background:var(--red)}
.badge.autonomous{background:var(--green)}
.badge.phase{background:var(--blue)}
.job-title{font-size:16px;font-weight:700;color:#555;line-height:26px}
.job-meta{font-size:14px;color:#666;line-height:20px}
.next{left:565px;top:1652px;font-size:12px;color:#555}

.advertise{left:719px;top:1080px;width:397px;height:131px;background:var(--white);border-radius:12px;overflow:hidden}
.advertise-head{height:56px;background:var(--blue-head);color:var(--white);font-weight:700;font-size:19px;display:flex;align-items:center;justify-content:center}
.advertise-body{height:75px;display:flex;align-items:center;justify-content:center;color:#666;font-weight:700;font-size:18px}

.filter-tabs{left:724px;top:1300px;display:flex}
.tab{width:110px;height:54px;display:flex;align-items:center;justify-content:center;font-size:18px;color:#444;background:var(--white)}
.tab.alt{background:#b5b5b5;color:var(--white);font-weight:700}
.filter-list{left:724px;top:1354px;width:389px;background:var(--white)}
.filter-list div{height:48px;border-bottom:1px solid #ddd;display:flex;justify-content:space-between;align-items:center;padding:0 18px;font-size:18px;color:#999}

.courses-title{left:903px;top:1640px;font-size:24px;color:#444}

.connect{left:0;top:1669px;width:637px;height:842px;background:var(--panel)}
.social{position:absolute;left:168px;width:437px;border-top:1px solid #ddd}
.social h3{font-size:28px;line-height:32px;font-weight:700;color:#333;margin-top:32px}
.social p{font-size:16px;color:#777;margin-top:4px}
.social .icon{position:absolute;right:0;top:30px;width:76px;height:76px;border-radius:50%}
.social.first h3{margin-top:51px}
.social.first .icon{top:40px}
.icon.orange{background:#f07b2a}
.icon.sky{background:#5fb4e8}
.icon.grey{background:#9a9a9a}
.icon.navy{background:#3d5a98}
.social-end{position:absolute;left:168px;top:604px;width:437px;border-top:1px solid #ddd}

.newsletter{left:220px;top:2310px;width:385px}
.newsletter h4{font-size:20px;font-weight:700;color:#333;margin-bottom:6px}
.newsletter-box{border:1px solid #c6d3e0;background:#eef2f6;height:102px;padding:8px 10px;font-size:13px;color:#444}
.newsletter-row{display:flex;align-items:center;gap:8px;margin-top:12px}
.newsletter-row .input{width:180px;height:26px;background:var(--white);border:1px solid #888}
.newsletter-btn{margin:8px auto 0;width:96px;height:26px;border:1px solid #888;background:#f4f4f4;border-radius:3px;display:flex;align-items:center;justify-content:center;font-size:15px}

.course-text{position:absolute;left:660px;width:225px;font-size:12px;line-height:19px;color:#333}
.course-ad{position:absolute;left:902px;width:266px;background:var(--white)}
.course-ad .photo{height:155px}
.course-ad .copy{padding:8px 10px;font-size:10px;line-height:13px;color:#333}
.course-ad .cta{display:inline-block;margin-top:8px;background:#e8541e;color:var(--white);font-size:10px;font-weight:700;padding:4px 10px}
.course-ad .mark{float:right;margin-top:10px;font-size:14px;font-weight:700;color:#e8541e}

.site-footer{left:0;top:2511px;width:1200px;height:98px;background:var(--white);text-align:center;font-size:13px;color:#444;padding-top:13px;line-height:22px}
.site-footer .copy{margin-top:14px}
</style>
</head>
<body>

<header class="masthead abs">
  <div class="brand"><span class="brand-dot"></span><span class="brand-name">Trilha Velora</span></div>
</header>

<nav class="main-nav abs">
  <span>Home</span><span>BLOG</span><span>For Professionals</span><span>For Business</span><span>Events &amp; Partners</span><span>About Us</span><span>Contact Us</span>
  <span class="spacer"></span>
  <span class="first-right">Advertise JOB VACANCY</span><span class="last">Log In/ Register</span>
</nav>

<div class="hero abs" role="img" aria-label="Photo of a businesswoman resting on the grass beside an open laptop"></div>

<div class="search-bar abs">
  <div class="search-type">Jobs <svg viewBox="0 0 18 14"><path d="M1 1h16L9 13z" fill="#777"/></svg></div>
  <div class="search-field"></div>
  <div class="search-field"></div>
  <div class="search-btn">SEARCH</div>
</div>

<div class="hero-gap abs"></div>

<div class="eyebrow abs">FEATURED</div>
<div class="listing-title abs">Latest Job Vacancies</div>
<div class="rss abs"></div>
<div class="rule abs" style="left:0;top:1069px;width:1200px"></div>

<section>
  <div class="job" style="top:1070px;height:107px"><span class="badge registered">Registered<br>(CTL)</span>
    <div class="job-title">Auxiliar Cabeleireiro (MASC/FEM.) – Maison Lirael – São (Bernardo do Campo (SP</div>
    <div class="job-meta">SALÃO MAISON LIRAEL SHOPP CENTRAL-SBC-SP – Publicado por Marisa</div></div>
  <div class="job" style="top:1177px;height:71px"><span class="badge registered">Registered<br>(CTL)</span>
    <div class="job-title">(Esteticista Facial e Corporal – Curicica – Rio de Janeiro (RJ</div>
    <div class="job-meta">Brisa Spa – Publicado por Brisa Spa</div></div>
  <div class="job" style="top:1248px;height:75px"><span class="badge autonomous">Autonomous</span>
    <div class="job-title">(Auxiliar de Cabeleireiro – Vila Rosália – Guarulhos (SP</div>
    <div class="job-meta">Bellora Cabelo e Estética – Publicado por bellora</div></div>
  <div class="job" style="top:1323px;height:74px"><span class="badge registered">Registered<br>(CTL)</span>
    <div class="job-title">(Estoquista – Maison Lirael – São Bernardo do Campo (SP</div>
    <div class="job-meta">Marisa – Publicado por Marisa</div></div>
  <div class="job" style="top:1397px;height:93px"><span class="badge autonomous">Autonomous</span>
    <div class="job-title">Hairdresser and Hairdresser Assistant - Campo Belo - São Paulo ((SP</div>
    <div class="job-meta">Lia Sato - Posted by Lia Sato</div></div>
  <div class="job" style="top:1490px;height:99px"><span class="badge phase">Phase</span>
    <div class="job-title">Trainee in aesthetic facial and body - Spa - São Paulo<br>((SP</div>
    <div class="job-meta">RK Spa - Posted by rkspa</div></div>
  <div class="job" style="top:1589px;height:80px"><span class="badge registered">Registered<br>(CTL)</span>
    <div class="job-title">(Stockist - Maison Lirael - São Bernardo do Campo (SP</div>
    <div class="job-meta">Marisa - Posted by Marisa</div></div>
  <div class="next abs">NEXT&gt;&gt;</div>
</section>

<aside>
  <div class="advertise abs">
    <div class="advertise-head">Advertise Job Vacancy</div>
    <div class="advertise-body">Advertise vacancy FREE</div>
  </div>
  <div class="rule abs" style="left:637px;top:1250px;width:563px"></div>
  <div class="filter-tabs abs"><div class="tab">Search by</div><div class="tab alt">Tags</div></div>
  <div class="filter-list abs">
    <div>Job Type<span>&gt;</span></div>
    <div>Salary Job<span>&gt;</span></div>
    <div>Job Category<span>&gt;</span></div>
    <div>Published Date<span>&gt;</span></div>
  </div>
  <div class="rule abs" style="left:637px;top:1589px;width:563px"></div>
  <div class="courses-title abs">Online Courses Aprendi</div>
</aside>

<section class="connect abs">
  <div class="social first" style="top:78px;height:146px"><h3>Subscribe</h3><p>Receive the latest jobs</p><span class="icon orange"></span></div>
  <div class="social" style="top:224px;height:110px"><h3>Follow Us</h3><p>Come join us on Chirply</p><span class="icon sky"></span></div>
  <div class="social" style="top:334px;height:126px"><h3>Follow us</h3><p>Come join us on Circlo</p><span class="icon grey"></span></div>
  <div class="social" style="top:460px;height:144px"><h3>Take part!</h3><p>Be part of our network on Rodanet</p><span class="icon navy"></span></div>
  <div class="social-end"></div>
</section>

<div class="newsletter abs">
  <h4>Subscribe Trilha Velora</h4>
  <div class="newsletter-box">
    Get latest Job Vacancies &amp; News.
    <div class="newsletter-row">Email Address <span class="input"></span></div>
    <div class="newsletter-btn">Subscribe!</div>
  </div>
</div>

<div class="course-text" style="top:1719px">The course of Makeup Techniques brings updated methods of makeup, with an emphasis on visagism and with different ethnic styles. The course also includes innovations in the areas of care, hygiene and organization to provide service salon,</div>
<div class="course-ad" style="top:1719px;height:267px">
  <div class="photo" role="img" aria-label="Close-up of a makeup brush with pink powder" style="background:linear-gradient(135deg,#3a2a30 0%,#b07a88 60%,#e7c3cc 100%)"></div>
  <div class="copy">Seja um profissional mais qualificado, invista na sua carreira e se prepare para o mercado de trabalho. Matricule-se no curso de Maquiagem.<br><span class="cta">EXPERIMENTE GRÁTIS</span><span class="mark">Aprendi</span></div>
</div>

<div class="course-text" style="top:2006px">O curso de cabeleireiro de Rui Fontana pode revolucionar o seu Studio. Além de técnicas de corte incríveis para diversos grupos étnicos e biotipos, dicas de visagismo, avaliação do cabelo e finalização, Rui fala sobre aspectos</div>
<div class="course-ad" style="top:2008px;height:267px">
  <div class="photo" role="img" aria-label="Hairdresser styling long hair in a salon" style="background:linear-gradient(135deg,#d9c3a8 0%,#a5805e 55%,#f0e6da 100%)"></div>
  <div class="copy">Seja um profissional mais qualificado, invista na sua carreira e se prepare para o mercado de trabalho. Matricule-se no curso de Cabeleireiro.<br><span class="cta">EXPERIMENTE GRÁTIS</span><span class="mark">Aprendi</span></div>
</div>

<footer class="site-footer abs">
  <div>Job Vacancies - Beauty:&nbsp; Aux Hairdresser&nbsp; |&nbsp; Aux Escovista&nbsp; |&nbsp; Hairdresser&nbsp; |&nbsp; epilator&nbsp; |&nbsp; Manicure&nbsp; |&nbsp; Makeup&nbsp; |&nbsp; Eyebrow Designer</div>
  <div>Job Vacancies - Health and Wellness:&nbsp; Esthetician&nbsp; |&nbsp; Massage Therapist&nbsp; |&nbsp; Podiatrist&nbsp; |&nbsp; Physiotherapist&nbsp; |&nbsp; Nurse</div>
  <div class="copy">Copyright 2013 @ Trilha Velora - Your Community for Professionals and Companies Beauty, Aesthetics and Wellness</div>
</footer>

</body>
</html>
```